Professional, Elegant, Modern and Playful business card Design for an Orthodontist (Dentist)

We need a new business card design for an Orthodontist (Dentist).
We would like to see designs that are elegant, but also playful. The designs and colors should be in harmony with the existing logo (uploaded).
Size: standard size (85mm x 55mm)
The font of the logo text is roboto (Google), you don't need to use the same font, but the used font has to be in harmony with the font used in the logo.
The colors used have to be in harmony with the logo.

Target Market(s)

Orthodontist (Dentist)

Industry/Entity Type

Dental Clinic

Contact Information for Business Card

* Size: standard size (85mm x 55mm)
* The font of the logo text is roboto (Google), you don't need to use the same font, but the used font has to be in harmony with the font used in the logo.
* The colors used have to be in harmony with the logo.

* Following Information have to be on the front side:
- Logo with company name (see uploaded files) as a unit
or
- separate the logo from the text and position them separately
- Text that has to be on the front side:
Kieferorthopädie Brunnweid
Dr. med. dent. Lukas Venberg
Fachzahnarzt für Kieferorthopädie (CH)
(if there is enough space, please also write:
Eidg. dipl. Zahnarzt, Mitglied VZB und FOV)
(address:)
Talackerweg 7
8946 Brunnwil
(telephone number:)
044 618 42 50
(if there is much space left, also fax number, but it is not mandatory:
044 618 42 51)
info@brunnweidpraxis.net
www.brunnweidpraxis.net
(If there is space left:
QR-code with the homepage-adress: www.brunnweidpraxis.net
and in the center of the QR-Code a little logo)
- It is important not to overload the front side. Put in the optional parts on the front side only if it doesn't look overloaded.

* Following Information have to be on the back side:
- An abstract map sketch (freehand drawing) of the location of the office is uploaded (Map on the back side of the business card.pdf). Please do a nicely designed abstract map based on this sketch.
- Feel free to change everything to make it good.
- For better reading the text has been rewritten in the sketch on the outside of the border of the card.
- You can see the original situation e.g. in google maps (Address: Talackerweg 7, 8946 Brunnwil, Switzerland)
- Marked as yellow are the important streets. These should not be yellow in the final design.
- The symbols of the freeway (green symbol) and the car park are uploaded ad vector graphics.
- "A1" should be the same green color as the background of the freeway (green symbol).
- The symbols of the bus stops and the railway station are uploaded as pixel graphics. Please convert them to vector graphics and make the background blue the same.
- The badges of the train numbers (S3 and S12) and bus numbers (31, 302, 303, 307, 308) are also pixel graphics. Please draw them as vector graphics. The font doesn't have to be identical with the one in the sketch, but the color codes need to be the same in the final design.
- The dashed blue line is a footway only. It should not be drawn like this in the final design. The design decision is up to you, but it should be different from the streets.
- The building of the office and the arrow showing the entrance should be clearly
visible and distinguishable form the other drawings.

Font styles to use
Sans Serif

Colors

Designer to choose colors to be used in the design.

Requirements
Must have
• - vector graphics
• - vector files: adobe illustrator or compatible
Should not have
• - pixel graphics

```html
<!DOCTYPE html>
<html lang="de">
<head>
<meta charset="utf-8">
<title>Kieferorthopädie Brunnweid – Visitenkarte</title>
<link rel="stylesheet" href="https://fonts.googleapis.com/css2?family=Roboto:wght@400;700&family=Open+Sans:wght@400&display=swap">
<style>
  :root {
    --sky: #55d6fb;
    --navy: #1b1b8e;
    --ink: #5e6a72;
    --paper: #ffffff;
    --backdrop: #ffffff;
  }
  html, body {
    margin: 0;
    padding: 0;
    width: 1200px;
    height: 804px;
    overflow: hidden;
    background: var(--backdrop);
  }
  .card {
    position: relative;
    width: 1200px;
    height: 804px;
    background: var(--paper);
    overflow: hidden;
    font-family: "Open Sans", Arial, sans-serif;
  }
  .card-shapes {
    position: absolute;
    inset: 0;
    width: 1200px;
    height: 804px;
  }
  .brand {
    position: absolute;
    left: 112px;
    top: 92px;
    display: flex;
    align-items: center;
    gap: 30px;
  }
  .brand-dot {
    width: 80px;
    height: 80px;
    border-radius: 50%;
    background: var(--sky);
    flex: none;
  }
  .brand-text {
    font-family: "Roboto", Arial, sans-serif;
    line-height: 1;
  }
  .practice-name {
    margin: 0 0 6px;
    font-size: 25px;
    font-weight: 700;
    color: var(--navy);
    letter-spacing: -0.2px;
  }
  .doctor-line {
    margin: 0 0 4px;
    font-size: 17px;
    font-weight: 400;
    color: var(--ink);
    letter-spacing: 0.3px;
  }
  .contact-list {
    position: absolute;
    left: 0;
    top: 0;
    margin: 0;
    padding: 0;
    list-style: none;
  }
  .contact-item {
    position: absolute;
    left: 150px;
    white-space: nowrap;
  }
  .contact-icon {
    position: absolute;
    left: 0;
    width: 36px;
    height: 36px;
    fill: var(--navy);
  }
  .contact-text {
    position: absolute;
    left: 89px;
    font-size: 31px;
    line-height: 44px;
    color: var(--ink);
  }
  .accent { color: var(--sky); }
  .item-address { top: 326px; }
  .item-address .contact-icon { top: 17px; }
  .item-phone { top: 434px; }
  .item-phone .contact-icon { top: 0; }
  .item-fax { top: 502px; }
  .item-fax .contact-icon { top: -6px; }
  .item-mail { top: 566px; }
  .item-mail .contact-icon { top: 4px; }
  .item-web { top: 642px; }
  .item-web .contact-icon { top: 4px; }
  .panel-name {
    position: absolute;
    left: 828px;
    width: 300px;
    top: 380px;
    margin: 0;
    text-align: center;
    font-family: "Roboto", Arial, sans-serif;
    font-weight: 700;
    font-size: 30px;
    color: var(--paper);
    letter-spacing: 0.5px;
  }
</style>
</head>
<body>
<main class="card">
  <svg class="card-shapes" viewBox="0 0 1080 724" preserveAspectRatio="none" aria-hidden="true">
    <rect class="edge-bar" x="35" y="35" width="15" height="650" fill="var(--sky)"/>
    <polygon class="chevron-stripe" fill="var(--sky)"
      points="685,35 708,35 800,128 632,360 797,685 775,685 612,360 785,128"/>
    <polygon class="chevron-panel" fill="var(--sky)"
      points="722,35 1040,35 1040,685 822,685 650,360 822,128"/>
  </svg>

  <header class="brand">
    <span class="brand-dot"></span>
    <div class="brand-text">
      <h1 class="practice-name">Kieferorthopädie Brunnweid</h1>
      <p class="doctor-line">Dr. med. dent. Lukas Venberg</p>
      <p class="doctor-line">Fachzahnarzt für Kieferorthopädie (CH)</p>
    </div>
  </header>

  <ul class="contact-list">
    <li class="contact-item item-address">
      <svg class="contact-icon" viewBox="0 0 24 24" aria-hidden="true">
        <path d="M12 1.5c-4.1 0-7.3 3.2-7.3 7.2 0 5.2 7.3 13.8 7.3 13.8s7.3-8.6 7.3-13.8c0-4-3.2-7.2-7.3-7.2zm0 10a2.8 2.8 0 1 1 0-5.6 2.8 2.8 0 0 1 0 5.6z"/>
      </svg>
      <span class="contact-text">Talackerweg 7<br>8946 <span class="accent">Brunnwil</span>.</span>
    </li>
    <li class="contact-item item-phone">
      <svg class="contact-icon" viewBox="0 0 24 24" aria-hidden="true">
        <path d="M6.6 2.2l2.6 4.1c.3.5.2 1.1-.2 1.5L7.4 9.3c1.3 2.9 3.5 5.1 6.3 6.4l1.6-1.6c.4-.4 1-.5 1.5-.2l4.1 2.6c.5.3.7 1 .4 1.5l-1.4 2.5c-.4.7-1.2 1.1-2 .9C10.6 20 4 13.4 2.6 6.1c-.2-.8.2-1.6.9-2l2.6-1.4c.2-.1.4-.5.5-.5z"/>
      </svg>
      <span class="contact-text">044 618 42 50</span>
    </li>
    <li class="contact-item item-fax">
      <svg class="contact-icon" viewBox="0 0 24 24" aria-hidden="true">
        <path d="M6 2h12v5H6zM3 8h18a2 2 0 0 1 2 2v7h-4v-3H5v3H1v-7a2 2 0 0 1 2-2zm3 7h12v7H6z"/>
      </svg>
      <span class="contact-text">044 618 42 51</span>
    </li>
    <li class="contact-item item-mail">
      <svg class="contact-icon" viewBox="0 0 24 24" aria-hidden="true">
        <path d="M1 4h22v16H1zm2 2v.3l9 6.2 9-6.2V6zm0 2.7V18h18V8.7l-9 6.2z"/>
      </svg>
      <span class="contact-text">info@brunnweidpraxis.net</span>
    </li>
    <li class="contact-item item-web">
      <svg class="contact-icon" viewBox="0 0 24 24" aria-hidden="true">
        <circle cx="12" cy="12" r="10.5"/>
        <g fill="none" stroke="#ffffff" stroke-width="1">
          <ellipse cx="12" cy="12" rx="4.5" ry="10.5"/>
          <line x1="12" y1="1.5" x2="12" y2="22.5"/>
          <line x1="1.5" y1="12" x2="22.5" y2="12"/>
          <path d="M3.2 6.5h17.6M3.2 17.5h17.6"/>
        </g>
      </svg>
      <span class="contact-text">www.<span class="accent">brunnweidpraxis</span>.net</span>
    </li>
  </ul>

  <p class="panel-name">Brunnweid</p>
</main>
</body>
</html>
```